Webdesign für KFZ-Service-Betrieb
Zielgruppe
Wartung, Reparatur und Instandsetzung von Kraftfahrzeugen aller Marken.
Reifenhandel, Old- und Youngtimer-Service, An- und Verkauf von Fahrzeugen.
Aufgabenstellung
Firmenfarbe ist blau.
Moderner, Übersichtlicher und Transparenter Auftritt erwünscht.

```html
<!DOCTYPE html>
<html lang="de">
<head>
<meta charset="utf-8">
<title>Der Feinmeister – Autoservice nach Maß</title>
<link href="https://fonts.googleapis.com/css2?family=Roboto:ital,wght@0,300;0,400;0,500;0,700;1,300&display=swap" rel="stylesheet">
<style>
:root{
  --blue:#0a2f9c;
  --grey-text:#777a80;
  --grey-band:#ececec;
  --panel:#cdd5e5;
  --panel-line:#b5bfd3;
  --white:#ffffff;
  --badge:#f7f7f7;
}
*{box-sizing:border-box;margin:0;padding:0}
html,body{width:1200px;height:1141px;overflow:hidden;background:var(--white);font-family:'Roboto',sans-serif}
.page{position:relative;width:1200px;height:1141px}
.abs{position:absolute}

/* header */
.header{left:0;top:0;width:1200px;height:62px;background:var(--white);border-bottom:1px solid #d9d9d9}
.brand{left:244px;top:17px;display:flex;align-items:center;gap:8px}
.brand-mark{width:26px;height:26px;border-radius:50%;background:var(--blue)}
.brand-name{font-size:19px;font-weight:400;color:var(--blue);line-height:1}
.brand-tag{display:block;font-size:8px;color:var(--blue);margin-top:3px;font-weight:400}
.contact{top:18px;font-size:10px;color:var(--grey-text);line-height:12.5px;text-align:right;font-weight:300}
.contact-mail{right:391px}
.contact-hours{right:244px}
.icon{top:18px}
.divider{left:821px;top:14px;width:1px;height:32px;background:#dedede}

/* nav */
.nav{left:0;top:63px;width:1200px;height:31px;background:var(--grey-band)}
.nav a{position:absolute;top:10px;font-size:10px;color:var(--grey-text);text-decoration:none;letter-spacing:.2px}
.nav a.active{color:var(--blue)}
.nav .underline{position:absolute;left:256px;top:29px;width:82px;height:2px;background:var(--white)}

/* hero */
.hero{left:0;top:94px;width:1200px;height:280px;background:linear-gradient(180deg,#8e9196 0%,#5f6166 45%,#6c6f74 75%,#a4a6a9 100%)}
.hero-overlay{left:0;top:176px;width:769px;height:118px;background:rgba(236,237,240,.86)}
.hero-title{left:244px;top:184px;font-size:27px;font-weight:700;color:var(--blue);letter-spacing:.2px}
.hero-text{left:244px;top:219px;font-size:10px;font-weight:500;color:var(--grey-text);line-height:12px;text-transform:uppercase}
.hero-text b{color:var(--blue)}
.btn{left:244px;top:251px;width:125px;height:28px;background:var(--blue);color:var(--white);font-size:10.5px;font-weight:500;display:flex;align-items:center;justify-content:center}
.dots{left:906px;top:357px;display:flex;gap:6px}
.dots span{width:8px;height:8px;border-radius:50%;border:1.3px solid var(--white)}
.dots span.on{background:var(--blue)}

/* brand strip */
.makes{left:0;top:374px;width:1200px;height:66px;background:var(--grey-band)}
.make{top:20px;width:26px;height:26px;border-radius:50%;background:#b9bcc3}
.make.sq{border-radius:4px;background:#c4c6cc}

/* services */
.section-title{left:0;top:466px;width:1200px;text-align:center;font-size:21px;font-weight:400;color:var(--blue)}
.tile{width:225px;height:125px;overflow:hidden;box-shadow:0 1px 2px rgba(0,0,0,.25)}
.tile-photo{position:absolute;inset:0}
.tile-label{position:absolute;left:9px;bottom:9px;font-size:14px;font-weight:500;color:var(--white);text-transform:uppercase}
.tile-arrow{position:absolute;right:10px;bottom:10px}
.partner-badge{position:absolute;left:28px;top:27px;width:169px;height:72px;background:var(--badge);border-radius:2px}

/* panels */
.panel{top:796px;width:347px;height:262px;background:var(--panel)}
.panel h2{position:absolute;left:9px;top:13px;font-size:13.5px;font-weight:500;color:var(--blue)}
.quote{position:absolute;left:9px;width:329px;border-bottom:1px dashed var(--panel-line)}
.avatar{position:absolute;left:1px;top:0;width:50px;height:50px;border-radius:50%;background:linear-gradient(160deg,#c9c5c2,#7c7b80)}
.quote p{position:absolute;left:63px;top:0;width:262px;font-size:9.5px;font-style:italic;font-weight:300;color:var(--grey-text);line-height:12px}
.quote p span{display:block;font-style:normal;font-weight:400;color:#444;font-size:10px}
.pdots{position:absolute;left:154px;top:240px;display:flex;gap:4px}
.pdots span{width:7px;height:7px;border-radius:50%;background:#8897c0}
.pdots span.on{background:var(--blue)}
.offers{position:absolute;left:10px;top:38px;width:329px;list-style:none}
.offers li{font-size:10px;color:#444;line-height:12px;padding:6px 0 9px 1px;border-bottom:1px dashed var(--panel-line);font-weight:400}
.offers li:last-child{border-bottom:none}

/* footer */
.footer{left:0;top:1089px;width:1200px;height:32px;background:var(--grey-band)}
.footer a{position:absolute;top:10px;font-size:10px;color:var(--grey-text);text-decoration:none;font-weight:300}
.footer a.active{color:var(--blue);font-weight:400}
.copy{left:0;top:1125px;width:1200px;text-align:center;font-size:8.5px;color:var(--grey-text);font-weight:300}
</style>
</head>
<body>
<div class="page">

  <header class="abs header">
    <div class="abs brand">
      <span class="brand-mark"></span>
      <div>
        <span class="brand-name">Der Feinmeister</span>
        <span class="brand-tag">Autoservice nach Maß</span>
      </div>
    </div>
    <svg class="abs icon" style="left:664px" width="20" height="22" viewBox="0 0 20 22" aria-hidden="true">
      <path d="M4 6c-2 2-1 7 3 11s8 4 9 2l-3-3-2 1c-2-1-4-3-5-5l1-2z" fill="var(--blue)"/>
      <text x="11" y="9" font-size="9" font-family="Roboto,sans-serif" font-weight="700" fill="var(--blue)">@</text>
    </svg>
    <div class="abs contact contact-mail">info@feinmeister-auto.de<br>01234 / 56 78</div>
    <div class="abs divider"></div>
    <svg class="abs icon" style="left:834px;top:19px" width="22" height="22" viewBox="0 0 22 22" aria-hidden="true">
      <circle cx="11" cy="11" r="9.5" fill="none" stroke="var(--blue)" stroke-width="2"/>
      <path d="M11 5v6l4 3" fill="none" stroke="var(--blue)" stroke-width="2" stroke-linecap="round"/>
    </svg>
    <div class="abs contact contact-hours">Mo-Fr: 07:30 - 18:00<br>Sa: 09:00 -12:00</div>
  </header>

  <nav class="abs nav">
    <a class="active" style="left:269px">STARTSEITE</a>
    <a style="left:362px">LEISTUNGEN</a>
    <a style="left:460px">PHILOSOPHIE</a>
    <a style="left:561px">FIRMENGESCHICHTE</a>
    <a style="left:696px">ZUFRIEDENE KUNDEN</a>
    <a style="left:834px">TEAM UND KONTAKT</a>
    <span class="underline"></span>
  </nav>

  <section class="abs hero" role="img" aria-label="Foto: gestapelte Sommerreifen in einer Werkstatt"></section>
  <div class="abs hero-overlay"></div>
  <h1 class="abs hero-title">SOMMERRÄDER KAUFEN!</h1>
  <p class="abs hero-text">Bei uns gibt es Markenreifen schon ab <b>39 €</b> Wir liefern alle Fabrikate zu günstigen Preisen.<br>Fragen Sie nach Ihren individuellen Angebot.</p>
  <a class="abs btn">CONTACT US</a>
  <div class="abs dots"><span class="on"></span><span></span><span></span><span></span></div>

  <section class="abs makes" aria-label="Fahrzeugmarken">
    <svg class="abs" style="left:235px;top:18px" width="12" height="30" viewBox="0 0 12 30" aria-hidden="true"><path d="M11 1L1 15l10 14" fill="none" stroke="#888" stroke-width="1.2"/></svg>
    <span class="abs make" style="left:272px"></span>
    <span class="abs make sq" style="left:321px;top:24px;height:16px;width:28px"></span>
    <span class="abs make" style="left:369px"></span>
    <span class="abs make sq" style="left:415px;top:30px;height:6px;width:32px"></span>
    <span class="abs make sq" style="left:466px;top:24px;height:18px"></span>
    <span class="abs make sq" style="left:515px;top:22px;height:22px;width:22px"></span>
    <span class="abs make sq" style="left:564px;top:19px;height:28px;width:22px"></span>
    <span class="abs make" style="left:613px;width:28px;height:28px;top:19px"></span>
    <span class="abs make sq" style="left:660px;top:22px;height:22px;width:24px"></span>
    <span class="abs make" style="left:711px;width:26px;height:18px;top:24px"></span>
    <span class="abs make sq" style="left:754px;top:24px;height:16px;width:32px"></span>
    <span class="abs make sq" style="left:802px;top:24px;height:16px;width:32px"></span>
    <span class="abs make" style="left:852px;width:28px;height:16px;top:25px"></span>
    <span class="abs make" style="left:901px;width:28px;height:28px;top:19px"></span>
    <svg class="abs" style="left:953px;top:18px" width="12" height="30" viewBox="0 0 12 30" aria-hidden="true"><path d="M1 1l10 14L1 29" fill="none" stroke="#888" stroke-width="1.2"/></svg>
  </section>

  <h2 class="abs section-title">LEISTUNGEN</h2>

  <a class="abs tile" style="left:244px;top:504px">
    <div class="tile-photo" role="img" aria-label="Foto: Mechaniker arbeitet unter einem Fahrzeug" style="background:linear-gradient(160deg,#8a8d90,#4a4b4f 60%,#2b2b2e)"></div>
    <span class="tile-label">Service</span>
    <svg class="tile-arrow" width="16" height="16" viewBox="0 0 16 16" aria-hidden="true"><circle cx="8" cy="8" r="7" fill="none" stroke="#fff"/><path d="M7 5l3 3-3 3" fill="none" stroke="#fff"/></svg>
  </a>
  <a class="abs tile" style="left:487px;top:504px">
    <div class="tile-photo" role="img" aria-label="Foto: Werkstatthalle mit Hebebühnen" style="background:linear-gradient(180deg,#c9ccd0,#8d949c 55%,#3d4048)"></div>
    <span class="tile-label">Unfallinstandsetzung</span>
    <svg class="tile-arrow" width="16" height="16" viewBox="0 0 16 16" aria-hidden="true"><circle cx="8" cy="8" r="7" fill="none" stroke="#fff"/><path d="M7 5l3 3-3 3" fill="none" stroke="#fff"/></svg>
  </a>
  <a class="abs tile" style="left:731px;top:504px">
    <div class="tile-photo" role="img" aria-label="Foto: Verkaufsgespräch am Schreibtisch" style="background:linear-gradient(150deg,#a48a62,#d6b98a 55%,#4b3d30)"></div>
    <span class="tile-label">Verkauf</span>
    <svg class="tile-arrow" width="16" height="16" viewBox="0 0 16 16" aria-hidden="true"><circle cx="8" cy="8" r="7" fill="none" stroke="#fff"/><path d="M7 5l3 3-3 3" fill="none" stroke="#fff"/></svg>
  </a>
  <a class="abs tile" style="left:244px;top:648px">
    <div class="tile-photo" role="img" aria-label="Foto: Fahrzeug in der Waschanlage" style="background:linear-gradient(90deg,#2d4c8c,#8b9098 50%,#2d4c8c)"></div>
    <span class="tile-label">Fahrzeugpflege</span>
    <svg class="tile-arrow" width="16" height="16" viewBox="0 0 16 16" aria-hidden="true"><circle cx="8" cy="8" r="7" fill="none" stroke="#fff"/><path d="M7 5l3 3-3 3" fill="none" stroke="#fff"/></svg>
  </a>
  <a class="abs tile" style="left:487px;top:648px">
    <div class="tile-photo" role="img" aria-label="Foto: Mechaniker beim Radwechsel" style="background:linear-gradient(150deg,#b3262b,#5a3a3a 45%,#3a3f57)"></div>
    <span class="tile-label">Kleine Preisliste</span>
    <svg class="tile-arrow" width="16" height="16" viewBox="0 0 16 16" aria-hidden="true"><circle cx="8" cy="8" r="7" fill="none" stroke="#fff"/><path d="M7 5l3 3-3 3" fill="none" stroke="#fff"/></svg>
  </a>
  <a class="abs tile" style="left:731px;top:648px">
    <div class="tile-photo" style="background:linear-gradient(180deg,#f1f1f1,#cfcfcf)"></div>
    <div class="partner-badge" role="img" aria-label="Partnerzeichen Pflegestation"></div>
    <span class="tile-label">Korrax - Service</span>
    <svg class="tile-arrow" width="16" height="16" viewBox="0 0 16 16" aria-hidden="true"><circle cx="8" cy="8" r="7" fill="none" stroke="#fff"/><path d="M7 5l3 3-3 3" fill="none" stroke="#fff"/></svg>
  </a>

  <section class="abs panel" style="left:244px">
    <h2>ZUFRIEDENE KUNDEN</h2>
    <div class="quote" style="top:36px;height:106px">
      <div class="avatar" role="img" aria-label="Porträtfoto eines Kunden"></div>
      <p>"Habe bei "Feinmeister" ein Auto für meine Frau gekauft und möchte mich auf diesem Weg nochmals für den hervorragenden Service und die zuvorkommende Art des Herrn Lindner bedanken. Ich kann dieses Autohaus nur weiterempfehlen. Nur selten findet man in der Autobranche noch solche aufrichtigen Geschäftspartner."<span>E. Brandt</span></p>
    </div>
    <div class="quote" style="top:142px;height:94px">
      <div class="avatar" style="top:12px" role="img" aria-label="Porträtfoto eines Kunden"></div>
      <p style="top:12px">"Ich möchte mich hiermit Ihren Bewertungen positiv anschließen. Bei Ihnen wird Kundenfreundlichkeit noch großgeschrieben. Ihr Preis-Leistungs-Verhältnis ist nahezu unschlagbar. Ich denke ich habe in Sachen Reifen und Service einen neuen Favoriten gefunden. "<span>K.L.</span></p>
    </div>
    <div class="pdots" style="top:246px"><span class="on"></span><span></span><span></span><span></span></div>
  </section>

  <section class="abs panel" style="left:609px">
    <h2>AKTUELLE ANGEBOTE</h2>
    <ul class="offers">
      <li>10-Punkte</li>
      <li>Frühjahrs-Check nur 19,90 €</li>
      <li>Rädereinlagerung nur 19,90 €</li>
      <li>Räderwäsche nur 16,00€</li>
      <li>Komplettversiegelung des Unterbodens mit KORRAX zum kalkulierten Festpreis ab 249,00 €</li>
      <li>Fahrzeugkomplett-aufbereitung inkl. Lackreinigung, Politur &amp; Lackversiegelung, Innenreinigung ab 149,00 €</li>
      <li>Markenreifen ab 39,00 €</li>
    </ul>
  </section>

  <footer class="abs footer">
    <a class="active" style="left:254px">Impressum</a>
    <a style="left:328px">Disclaimer</a>
    <a style="left:399px">E-Mail</a>
    <a style="left:450px">Sitemap</a>
    <a style="left:511px">Login</a>
  </footer>
  <p class="abs copy">© Copyright 2016 Der Feinmeister GmbH</p>
</div>
</body>
</html>
```